Contractor Business Card Design

Looking to have a card made that has a bold description of (KITCHENS, BASEMENTS, BATHROOMS)

Definition and layers a plus

Contact info is;

Mark T. Ellery
Lakeport, MN 55000
Cell: 612-555-0147
website: www.cobaltfinishworks.example
Email: cobaltfinishworksmn@mailbox.example

colors: red, black, gray, white

Contact Information for Business Card

Contact info is;

Mark T. Ellery
Lakeport, MN 55000
Cell: 612-555-0147

Colors
ec1f27

Requirements
Must have
• Looking for layers and definition
Nice to have
• Cards are planned to be printed on plastic cards

```html
<!DOCTYPE html>
<html lang="en">
<head>
<meta charset="utf-8">
<title>Cobalt Finish Works – Business Card</title>
<link href="https://fonts.googleapis.com/css2?family=Poppins:wght@400;600;700&display=swap" rel="stylesheet">
<style>
  :root {
    --brand-red: #ec1f27;
    --card-black: #141414;
    --stage-dark: #1c1c1c;
    --stage-light: #2b2b2b;
    --ink-white: #ffffff;
    --ink-gray: #8e8e8e;
  }
  * { box-sizing: border-box; margin: 0; padding: 0; }
  html, body { width: 1200px; height: 1200px; overflow: hidden; }
  body {
    background: radial-gradient(circle at 60% 30%, var(--stage-light), var(--stage-dark) 70%);
    font-family: "Poppins", sans-serif;
    position: relative;
  }
  .card {
    position: absolute;
    left: 180px;
    width: 840px;
    height: 480px;
    background: var(--card-black);
    border-radius: 22px;
    overflow: hidden;
    box-shadow: 0 18px 40px rgba(0,0,0,.55);
  }
  .card--back { top: 80px; }
  .card--front { top: 620px; }

  /* back */
  .back-brand {
    position: absolute; left: 0; right: 0; top: 150px;
    display: flex; flex-direction: column; align-items: center; gap: 26px;
  }
  .back-brand__ring {
    width: 110px; height: 110px; border-radius: 50%;
    border: 4px solid var(--ink-gray);
  }
  .back-brand__name {
    color: var(--ink-gray); font-weight: 700; font-size: 40px; letter-spacing: 4px;
  }
  .services {
    display: flex; align-items: center; gap: 16px;
    font-weight: 700; letter-spacing: 1px; text-transform: uppercase;
  }
  .services__dot {
    width: 18px; height: 18px; border-radius: 50%;
    border: 2px solid currentColor;
  }
  .card--back .services {
    position: absolute; bottom: 60px; left: 0; right: 0; justify-content: center;
    color: var(--ink-white); font-size: 20px;
  }
  .card--back .services__dot { color: var(--brand-red); }

  /* front */
  .front-brand {
    position: absolute; left: 60px; top: 50px;
    color: var(--ink-white); font-weight: 700; font-size: 44px; letter-spacing: 3px; line-height: 1.1;
  }
  .contact {
    position: absolute; left: 60px; top: 190px; color: var(--ink-white);
  }
  .contact__name { font-weight: 600; font-size: 24px; letter-spacing: 1px; margin-bottom: 10px; }
  .contact__row {
    display: flex; align-items: center; gap: 12px; font-size: 19px; line-height: 1.6;
  }
  .contact__row svg { width: 18px; height: 18px; flex: none; fill: var(--brand-red); }
  .service-band {
    position: absolute; left: 0; bottom: 58px; width: 560px; height: 50px;
    background: linear-gradient(90deg, var(--brand-red) 75%, rgba(236,31,39,0));
    display: flex; align-items: center; padding-left: 40px;
  }
  .service-band .services { color: var(--ink-white); font-size: 21px; }
</style>
</head>
<body>

<section class="card card--back">
  <div class="back-brand">
    <div class="back-brand__ring"></div>
    <div class="back-brand__name">COBALT FINISH WORKS</div>
  </div>
  <div class="services">
    <span>Kitchens</span><span class="services__dot"></span>
    <span>Basements</span><span class="services__dot"></span>
    <span>Bathrooms</span>
  </div>
</section>

<section class="card card--front">
  <div class="front-brand">COBALT<br>FINISH WORKS</div>

  <div class="contact">
    <div class="contact__name">MARK T. ELLERY</div>
    <div class="contact__row">
      <svg viewBox="0 0 24 24"><path d="M7 1h10a2 2 0 0 1 2 2v18a2 2 0 0 1-2 2H7a2 2 0 0 1-2-2V3a2 2 0 0 1 2-2zm0 3v14h10V4zm5 15.5a1.2 1.2 0 1 0 0 2.4 1.2 1.2 0 0 0 0-2.4z"/></svg>
      <span>612-555-0147</span>
    </div>
    <div class="contact__row">
      <svg viewBox="0 0 24 24"><path d="M2 5h20v14H2zm2 2v.4l8 5.6 8-5.6V7zm0 2.8V17h16V9.8l-8 5.6z"/></svg>
      <span>cobaltfinishworksmn@mailbox.example</span>
    </div>
    <div class="contact__row">
      <svg viewBox="0 0 24 24"><path d="M12 1a8 8 0 0 0-8 8c0 6 8 14 8 14s8-8 8-14a8 8 0 0 0-8-8zm0 11a3 3 0 1 1 0-6 3 3 0 0 1 0 6z"/></svg>
      <span>Lakeport, MN 55000</span>
    </div>
  </div>

  <div class="service-band">
    <div class="services">
      <span>Kitchens</span><span class="services__dot"></span>
      <span>Basements</span><span class="services__dot"></span>
      <span>Bathrooms</span>
    </div>
  </div>
</section>

</body>
</html>
```